marlow pennant website Redesign

Read the Company mission statement and then help us redesign the website along the guidelines in the design brief and using the logo and fonts supplied.

The current marlow pennant website is very dated but has been very sucessful, we would like to invest in a brand refresh and site rebuild to bring the website up to 2018 standard.

We have using cut and paste from other travel websites made a pdf mock up of what sort of content we need on the pages and the lay out we like.

Target Market(s)

+45 Plus experienced Marlow Pennant, established, educated

Number of Pages Required

4 page

Font styles to use
Sans Serif

Requirements
Must have
• There is a full brief document and mock up, it must follow the brand guidelines
Nice to have
• There is a full brief document and mock up
Should not have
• Looks of a cheap cruise deal travel site

```html
<!DOCTYPE html>
<html lang="en">
<head>
<meta charset="utf-8">
<title>Marlow Pennant</title>
<link href="https://fonts.googleapis.com/css2?family=Open+Sans:wght@400;600;700&family=Kaushan+Script&display=swap" rel="stylesheet">
<style>
:root{
  --navy:#163a5f;
  --navy-deep:#0f2d4c;
  --green:#5fb672;
  --lime:#a9cf7c;
  --sky:#62b7df;
  --paper:#f1f1f1;
  --white:#ffffff;
  --charcoal:#333333;
  --text:#555a60;
  --muted:#8a8f94;
  --line-blue:#7fa3c8;
}
*{box-sizing:border-box;margin:0;padding:0}
html,body{width:1200px;height:4557px;overflow:hidden}
body{position:relative;background:var(--paper);font-family:"Open Sans",Arial,sans-serif;color:var(--text)}
.abs{position:absolute}
.heading{position:absolute;left:0;width:1200px;text-align:center;font-weight:700;color:var(--navy);font-size:46px}
.photo{position:absolute}

/* hero */
.hero{left:0;top:0;width:1200px;height:608px;background:linear-gradient(180deg,#24516a 0%,#3d7a7e 35%,#2b8fb0 60%,#7c9a7a 80%,#a8a98d 100%)}
.topbar{left:150px;top:8px;color:var(--white);font-weight:700;font-size:17px;display:flex;align-items:center;gap:8px}
.account{right:150px;top:8px;color:var(--white);font-size:16px;font-weight:600;display:flex;gap:10px;align-items:center}
.dot{width:20px;height:20px;border-radius:50%;background:var(--green);display:inline-block}
.brand{left:148px;top:52px;color:var(--white);font-weight:700;font-size:34px;line-height:1;letter-spacing:1px}
.nav{left:513px;top:46px;display:flex;gap:22px;align-items:center;color:var(--white);font-size:17px;font-weight:600}
.nav .cta{border:2px solid var(--white);padding:3px 10px;background:rgba(15,45,76,.6)}
.hero-panel{left:247px;top:292px;width:680px;height:150px;background:rgba(15,45,76,.75)}
.hero-title{left:0;top:20px;width:680px;text-align:center;color:var(--white);font-size:44px;font-weight:700}
.hero-title em{font-family:"Kaushan Script",cursive;font-style:normal;font-weight:400}
.search-input{left:24px;top:92px;width:523px;height:44px;background:#f5f5f5;color:#888;font-size:15px;padding:11px 14px}
.search-btn{left:547px;top:92px;width:124px;height:44px;background:var(--green);color:var(--white);font-size:17px;text-align:center;line-height:44px}

/* filters */
.filters{left:0;top:608px;width:1200px;height:140px;background:var(--lime);border-bottom:6px solid var(--line-blue)}
.select{position:absolute;width:180px;height:38px;background:var(--white);font-size:14px;color:#333;padding:9px 12px}
.select::after{content:"";position:absolute;right:12px;top:16px;border:6px solid transparent;border-top-color:#333}
.go{position:absolute;width:180px;height:38px;background:var(--navy);color:var(--white);font-size:15px;font-weight:600;text-align:center;line-height:38px}

/* welcome */
.welcome-title{left:150px;top:792px;font-size:46px;font-weight:700;color:var(--navy)}
.welcome-copy{left:150px;top:864px;width:640px;font-size:15.5px;line-height:27px;color:var(--text)}
.framed{border:8px solid var(--white);box-shadow:0 0 3px rgba(0,0,0,.15)}
.review{left:150px;top:1094px;width:890px;height:70px;background:var(--white)}
.stars{left:12px;top:18px;display:flex;gap:6px}
.quote{left:275px;top:22px;font-size:18px;color:var(--navy)}
.quote span{color:var(--muted);font-size:15px}
.more-btn{position:absolute;background:var(--green);color:var(--white);font-size:14px;text-align:center}

/* news */
.news-title{left:602px;font-size:36px;font-weight:700;color:var(--navy);line-height:42px;width:420px}
.news-copy{left:602px;width:430px;font-size:15px;line-height:23px;color:var(--muted)}
.divider{left:150px;width:890px;height:4px;background:linear-gradient(90deg,var(--line-blue),var(--lime))}

/* experiences */
.exp-label{width:260px;text-align:center;font-size:23px;font-weight:700;color:var(--navy)}

/* destinations */
.dest{left:0;top:2606px;width:1200px;height:622px;background:var(--charcoal);border-top:14px solid var(--line-blue)}
.card{position:absolute;top:160px;width:274px;height:402px;background:var(--white);padding:18px}
.card h3{margin-top:182px;font-size:24px;color:var(--navy);font-weight:700}
.card p{font-size:15px;line-height:22px;color:var(--muted);margin-top:4px}
.card .more-btn{left:65px;top:354px;width:144px;height:32px;line-height:32px}

/* marketing */
.brochure{position:absolute;top:3398px;width:217px;height:295px;background:var(--white);padding:10px}
.brochure .label{position:absolute;left:10px;bottom:10px;width:197px;height:58px;background:var(--sky);color:var(--navy);font-size:21px;text-align:center;line-height:58px}
.promo{top:3726px;font-size:20px;font-weight:700;color:var(--navy)}

/* newsletter */
.news-box{left:150px;top:3950px;width:890px;height:138px;background:#e4e4e4}
.email{left:93px;top:47px;width:541px;height:44px;background:var(--white);border:1px solid #ccc;color:#999;font-size:15px;padding:11px 14px}
.subscribe{left:665px;top:47px;width:212px;height:44px;background:var(--green);color:var(--white);font-size:18px;text-align:center;line-height:44px}
.badge{position:absolute;top:4138px;width:110px;height:100px;border-radius:14px;background:#d2d4d6}

/* footer */
.footer{left:0;top:4272px;width:1200px;height:250px;background:linear-gradient(180deg,#1d4e76,#153f63)}
.footer h4{position:absolute;top:42px;color:var(--white);font-size:16px;font-weight:600}
.footer p{position:absolute;top:78px;width:200px;color:#b9c8d8;font-size:13px;line-height:19px}
.legal{left:0;top:4522px;width:1200px;height:35px;background:var(--navy-deep);color:#9fb2c6;font-size:12px}
</style>
</head>
<body>

<header class="abs hero">
  <div class="photo" role="img" aria-label="Aerial photo of a turquoise bay beside a green rocky coastline" style="left:0;top:0;width:1200px;height:608px;background:linear-gradient(160deg,rgba(20,60,80,.5),rgba(60,150,160,.2) 50%,rgba(160,160,130,.4))"></div>
  <div class="abs topbar">
    <svg width="18" height="18" viewBox="0 0 24 24"><path fill="#fff" d="M6.6 10.8a15 15 0 0 0 6.6 6.6l2.2-2.2a1 1 0 0 1 1-.25 11.4 11.4 0 0 0 3.6.57 1 1 0 0 1 1 1V20a1 1 0 0 1-1 1A17 17 0 0 1 3 4a1 1 0 0 1 1-1h3.5a1 1 0 0 1 1 1c0 1.25.2 2.45.57 3.57a1 1 0 0 1-.25 1z"/></svg>
    1800 555 0142
  </div>
  <div class="abs account">Login <span>|</span> Sign up <span>|</span>
    <i class="dot"></i><i class="dot"></i><i class="dot"></i>
  </div>
  <div class="abs brand">Marlow<br>Pennant</div>
  <nav class="abs nav">
    <span>Home</span><span>Meet the Team</span><span>Specials</span><span>Contact</span><span class="cta">Request a Brochure</span>
  </nav>
  <div class="abs hero-panel">
    <div class="abs hero-title">Travel with <em>Personality</em></div>
    <div class="abs search-input">Where would you like to go?</div>
    <div class="abs search-btn">Search</div>
  </div>
</header>

<section class="abs filters">
  <div class="select" style="left:218px;top:30px">Any Destination</div>
  <div class="select" style="left:412px;top:30px">Any Sailing Date</div>
  <div class="select" style="left:606px;top:30px">Any Length</div>
  <div class="select" style="left:800px;top:30px">Any Destination</div>
  <div class="select" style="left:218px;top:80px">Any Cruise Ship</div>
  <div class="select" style="left:412px;top:80px">Any Departure Point</div>
  <div class="select" style="left:606px;top:80px">Any Price Range</div>
  <div class="go" style="left:800px;top:80px">Search Cruises &#9906;</div>
</section>

<section>
  <h1 class="abs welcome-title">Welcome to Marlow Pennant</h1>
  <p class="abs welcome-copy">Cum sociis natoque penatibus et magnis dis parturient montes, nascetur ridiculus mus. Nullam eleifend pharetra felis. Mauris nibh velit, tristique ac, lacinia in, scelerisque et, ante. Donec viverra tortor sed nulla. Phasellus nec magna. Aenean vehicula, turpis in congue eleifend, mauris lorem aliquam sem, eu eleifend est odio et pede. Mauris vitae mauris sit amet est rhoncus laoreet. Curabitur facilisis, urna vel egestas vulputate, tellus purus accumsan ante, quis</p>
  <div class="photo framed" role="img" aria-label="Calm alpine lake with forested mountains" style="left:815px;top:805px;width:228px;height:240px;background:linear-gradient(180deg,#9fc2df 0%,#6f8fa8 45%,#3d5a6e 60%,#9db8cc 100%)"></div>

  <div class="abs review">
    <div class="abs stars">
      <svg width="240" height="36" viewBox="0 0 240 36" fill="#163a5f"><g id="s"><path d="M18 1l5 11 12 1-9 8 3 12-11-6-11 6 3-12-9-8 12-1z"/></g><use href="#s" x="48"/><use href="#s" x="96"/><use href="#s" x="144"/><use href="#s" x="192"/></svg>
    </div>
    <div class="abs quote">"Friendly, reliable, trusted, great to deal with." <span>Ruth K, VIC</span></div>
    <div class="more-btn" style="left:742px;top:17px;width:136px;height:34px;line-height:34px">Read More Reviews</div>
  </div>
</section>

<section>
  <h2 class="heading" style="top:1210px">Travel News</h2>
  <div class="photo framed" role="img" aria-label="Small river ship moored beneath a cable bridge at sunset" style="left:152px;top:1307px;width:416px;height:325px;background:linear-gradient(180deg,#c9b98f 0%,#9aa6a2 45%,#6f8c8e 70%,#3f5f62 100%)"></div>
  <h3 class="abs news-title" style="top:1322px">Small ships are best!</h3>
  <p class="abs news-copy" style="top:1376px">liquam dapibus ipsum vitae sem. Ut eget mauris ac nunc luctus ornare. Phasellus enim augue, rutrum tempus, blandit in, vehicula eu, neque. Sed consequat nunc. Proin metus. Duis at mi non tellus malesuada tincidunt. Cras in neque. Sed lacinia, felis ut sodales pretium, justo sapien hendrerit est, et convallis nisi quam sit amet erat. Suspendisse consequat nibh a mauris. Curabitur libero ligula, faucibus at, mollis ornare, mattis et, libero.</p>
  <p class="abs news-copy" style="top:1580px">Aliquam pulvinar congue pede. Fusce condimentum turpis vel dolor. Ut blandit. Sed elementum justo quis sem. Sed eu</p>

  <div class="photo framed" role="img" aria-label="Sea turtle swimming over a reef in clear blue water" style="left:152px;top:1717px;width:416px;height:320px;background:linear-gradient(180deg,#2f8a9a 0%,#2a6f74 50%,#5a7b5e 100%)"></div>
  <h3 class="abs news-title" style="top:1728px">You won't find it elsewhere</h3>
  <p class="abs news-copy" style="top:1820px">liquam dapibus ipsum vitae sem. Ut eget mauris ac nunc luctus ornare. Phasellus enim augue, rutrum tempus, blandit in, vehicula eu, neque. Sed consequat nunc. Proin metus. Duis at mi non tellus malesuada tincidunt. Cras in neque. Sed lacinia, felis ut sodales pretium, justo sapien hendrerit est, et convallis nisi quam sit amet erat. Suspendisse consequat nibh a mauris. Curabitur libero ligula, faucibus at, mollis ornare, mattis et, libero.</p>
  <div class="abs divider" style="top:2110px"></div>
</section>

<section>
  <h2 class="heading" style="top:2164px">Amazing Range of Experiences</h2>
  <div class="photo framed" role="img" aria-label="River winding through misty mountains" style="left:115px;top:2273px;width:220px;height:220px;background:linear-gradient(180deg,#b9cde0,#7d97a8 55%,#4c6470)"></div>
  <div class="photo framed" role="img" aria-label="Hand holding a compass outdoors" style="left:365px;top:2273px;width:220px;height:220px;background:linear-gradient(160deg,#8d8a6a,#b08a67 55%,#5f6e58)"></div>
  <div class="photo framed" role="img" aria-label="Sunset over a calm ocean horizon" style="left:615px;top:2273px;width:220px;height:220px;background:linear-gradient(180deg,#3c4b5e,#d79a5a 50%,#2f3e4e)"></div>
  <div class="photo framed" role="img" aria-label="Large white luxury yacht on open water" style="left:864px;top:2273px;width:220px;height:220px;background:linear-gradient(180deg,#8fb6d8,#e6eef4 55%,#2f6f9c)"></div>
  <div class="abs exp-label" style="left:95px;top:2512px">River Cruises</div>
  <div class="abs exp-label" style="left:345px;top:2512px">Expedition Cruises</div>
  <div class="abs exp-label" style="left:595px;top:2512px">Fly Free Cruises</div>
  <div class="abs exp-label" style="left:844px;top:2512px">Luxury Cruises</div>
</section>

<section class="abs dest">
  <h2 class="heading" style="top:62px;color:var(--white)">Popular Destinations</h2>
  <div class="card" style="left:152px">
    <div class="photo" role="img" aria-label="City skyline with a tall tower lit up at night" style="left:18px;top:18px;width:238px;height:168px;background:linear-gradient(180deg,#0d1530,#2a2f6a 60%,#c04a6a)"></div>
    <h3>Sed lacinia, felis ut</h3>
    <p>liquam dapibus ipsum vitae sem. Ut eget mauris ac nunc luctus ornare. Phasellus enim augue, rutrum tempus, blandit in.</p>
    <div class="more-btn">Read More</div>
  </div>
  <div class="card" style="left:459px">
    <div class="photo" role="img" aria-label="Overwater villas above a turquoise lagoon" style="left:18px;top:18px;width:238px;height:168px;background:linear-gradient(180deg,#9fd3e6,#3fc1c4 55%,#6fa8a0)"></div>
    <h3>Sed lacinia, felis ut</h3>
    <p>liquam dapibus ipsum vitae sem. Ut eget mauris ac nunc luctus ornare. Phasellus enim augue, rutrum tempus, blandit in.</p>
    <div class="more-btn">Read More</div>
  </div>
  <div class="card" style="left:766px">
    <div class="photo" role="img" aria-label="Hillside village above a river" style="left:18px;top:18px;width:238px;height:168px;background:linear-gradient(180deg,#aebfcc,#8c8f80 50%,#5a7a8a)"></div>
    <h3>Sed lacinia, felis ut</h3>
    <p>liquam dapibus ipsum vitae sem. Ut eget mauris ac nunc luctus ornare. Phasellus enim augue, rutrum tempus, blandit in.</p>
    <div class="more-btn">Read More</div>
  </div>
</section>

<section>
  <h2 class="heading" style="top:3276px">Recent Marketing</h2>
  <div class="brochure" style="left:122px"><div class="photo" role="img" aria-label="River cruise brochure cover" style="left:10px;top:10px;width:197px;height:217px;background:linear-gradient(180deg,#2a4a8a,#c0b07a 45%,#7a9ab0)"></div><div class="label">Danube Deslights</div></div>
  <div class="brochure" style="left:370px"><div class="photo" role="img" aria-label="Europe fly free brochure cover" style="left:10px;top:10px;width:197px;height:217px;background:linear-gradient(180deg,#c62a2a,#e9d8c0 45%,#7a8aa0)"></div><div class="label">Fly Free Europe</div></div>
  <div class="brochure" style="left:617px"><div class="photo" role="img" aria-label="Canada fly free brochure cover" style="left:10px;top:10px;width:197px;height:217px;background:linear-gradient(180deg,#3a8ac8,#2a6a5a 50%,#c8d4de)"></div><div class="label">Fly Free Canada</div></div>
  <div class="brochure" style="left:860px"><div class="photo" role="img" aria-label="River cruise brochure cover" style="left:10px;top:10px;width:197px;height:217px;background:linear-gradient(180deg,#2a4a8a,#c0b07a 45%,#7a9ab0)"></div><div class="label">Danube Delights</div></div>
  <div class="abs promo" style="left:128px">&#8249;Last Weeks Promotions</div>
  <div class="abs promo" style="left:617px">This Weeks Promotions</div>
  <div class="abs divider" style="top:3810px"></div>
</section>

<section>
  <h2 class="heading" style="top:3858px">Newsletter Sign Up</h2>
  <div class="abs news-box">
    <div class="abs email">email address</div>
    <div class="abs subscribe">Subscribe</div>
  </div>
  <div class="badge" style="left:72px"></div>
  <div class="badge" style="left:240px"></div>
  <div class="badge" style="left:440px"></div>
  <div class="badge" style="left:640px"></div>
  <div class="badge" style="left:810px"></div>
  <div class="badge" style="left:1000px"></div>
</section>

<footer class="abs footer">
  <div class="abs brand" style="top:56px;font-size:30px">Marlow<br>Pennant</div>
  <div class="abs" style="left:150px;top:140px;display:flex;gap:10px"><i class="dot"></i><i class="dot"></i><i class="dot"></i></div>
  <div class="abs topbar" style="top:190px;font-size:19px">
    <svg width="18" height="18" viewBox="0 0 24 24"><path fill="#fff" d="M6.6 10.8a15 15 0 0 0 6.6 6.6l2.2-2.2a1 1 0 0 1 1-.25 11.4 11.4 0 0 0 3.6.57 1 1 0 0 1 1 1V20a1 1 0 0 1-1 1A17 17 0 0 1 3 4a1 1 0 0 1 1-1h3.5a1 1 0 0 1 1 1c0 1.25.2 2.45.57 3.57a1 1 0 0 1-.25 1z"/></svg>
    1800 555 0163
  </div>
  <h4 style="left:436px">Who We Are</h4>
  <p style="left:436px">Maecenas vitae erat. Ut ac purus vel purus dapibus gravida. Nullam lorem sapien, tempus ac, fringilla at, elementum sed purus. Duis mattis iaculis. Vivamus quis</p>
  <h4 style="left:676px">What We Do</h4>
  <p style="left:676px">Vestibulum ante ipsum primis in faucibus orci luctus et ultrices posuere cubilia Curae; Pellentesque sit amet metus. Nullam tincidunt posuere ligula.</p>
  <h4 style="left:915px">Contacts</h4>
  <p style="left:915px">14 Harbour Row, Sydney<br>NSW 2000 Australia<br><br>Support<br><span style="color:#fff">1800 555 0187</span></p>
</footer>
<div class="abs legal"><span class="abs" style="right:150px;top:10px">© Marlow Pennant 2018. All Rights Reserved.</span></div>

</body>
</html>
```